Shop window posters and banners for a contact lens (Carlow&Birkett Velora Pro)

Please take a look at our appearance on Instagram (optique_valmire), where you can also see the shop windows. In this case we would like to advertise a specific contact lens in the shop window. For this we need a poster and a banner. I can send you pictures of the lens. The poster banner should be filled with questions such as: Are you already wearing High Quality? Does your lens also have a blue filter? Feel good even after wearing it for a long time? Make an appointment with our vision experts!

Target Market(s)

Reach people who are dissatisfied with their contact lenses at the end of the day. For whom it may be important to protect their eyes from blue light.

Requirements
Must have
• correspond to the style of the store

```html
<!DOCTYPE html>
<html lang="en">
<head>
<meta charset="utf-8">
<title>Carlow&amp;Birkett Velora Pro – Shop Window Poster</title>
<link href="https://fonts.googleapis.com/css2?family=Poppins:wght@500;600;800&display=swap" rel="stylesheet">
<style>
  :root {
    --white: #ffffff;
    --sky: #62b6f2;
    --blue-top: #64b7f3;
    --blue-mid: #3d98e4;
    --blue-deep: #0668c8;
    --photo-cool: #9fb4bf;
    --photo-light: #dfe7ea;
    --photo-skin: #f1cdb9;
    --photo-warm: #e7a98d;
  }
  * { margin: 0; padding: 0; box-sizing: border-box; }
  html, body {
    width: 848px; height: 1200px; overflow: hidden;
    background: var(--white);
  }
  .poster {
    position: relative;
    width: 848px; height: 1200px;
    overflow: hidden;
    font-family: "Poppins", sans-serif;
    color: var(--white);
  }
  .hero-photo {
    position: absolute; inset: 0 0 auto 0;
    height: 760px;
    background:
      radial-gradient(ellipse 240px 200px at 470px 300px, #f6ddd0 0%, transparent 70%),
      linear-gradient(100deg, var(--photo-cool) 0%, var(--photo-light) 32%, var(--photo-skin) 55%, var(--photo-warm) 100%);
  }
  .waves { position: absolute; inset: 0; width: 848px; height: 1200px; }
  .question {
    position: absolute;
    text-align: center;
    font-weight: 600;
    font-size: 38px;
    line-height: 39px;
    letter-spacing: -0.2px;
    white-space: nowrap;
  }
  .question--quality { left: 182px; width: 360px; top: 622px; }
  .question--filter  { left: 470px; width: 366px; top: 762px; }
  .question--comfort { left: 40px;  width: 444px; top: 851px; }
  .call-to-action {
    position: absolute;
    left: 0; width: 848px; top: 1030px;
    text-align: center;
    font-weight: 800;
    font-size: 59px;
    line-height: 70px;
    letter-spacing: -0.5px;
    text-transform: uppercase;
    white-space: nowrap;
  }
</style>
</head>
<body>
<main class="poster">
  <div class="hero-photo" role="img" aria-label="Close-up photo of a person placing a clear contact lens on a fingertip towards a brown eye"></div>

  <svg class="waves" viewBox="0 0 848 1200" aria-hidden="true">
    <defs>
      <linearGradient id="panelBlue" x1="0" y1="460" x2="0" y2="1200" gradientUnits="userSpaceOnUse">
        <stop offset="0" stop-color="var(--blue-top)"/>
        <stop offset="0.35" stop-color="var(--blue-top)"/>
        <stop offset="0.6" stop-color="var(--blue-mid)"/>
        <stop offset="1" stop-color="var(--blue-deep)"/>
      </linearGradient>
    </defs>
    <path class="wave-white" fill="var(--white)"
          d="M0,690 C120,590 300,505 470,512 C600,518 700,470 848,345 L848,1200 L0,1200 Z"/>
    <path class="wave-sky" fill="var(--sky)"
          d="M0,800 C110,660 280,560 470,540 C620,525 740,500 848,415 L848,1200 L0,1200 Z"/>
    <path class="wave-line" fill="var(--white)"
          d="M0,925 C45,745 170,615 470,555 C620,522 760,495 848,455 L848,1200 L0,1200 Z"/>
    <path class="panel" fill="url(#panelBlue)"
          d="M0,945 C40,765 170,630 470,565 C620,532 760,505 848,465 L848,1200 L0,1200 Z"/>
  </svg>

  <p class="question question--quality">Are you<br>already&nbsp; wearing<br>High Quality?</p>
  <p class="question question--filter">Does your<br>lens also have a<br>blue filter?</p>
  <p class="question question--comfort">Feel good<br>even after wearing<br>it for a long time?</p>

  <h1 class="call-to-action">Make an appointment<br>with our vision experts!</h1>
</main>
</body>
</html>
```